Want to market to schools to offer free chair massages for teacher and staff of the schools

This postcard will be mailed to all public schools in the U.S.

We want the schools to call our company to have a massage therapist provide free chair massages to the teachers and staff at their next School Improvement or Teacher Institute day.

want to make the postcard fun and inviting.

The postcard is 4 1/4" X 6"

FRONT AND BACK DESIGN.

For the back of postcard design, I have attached a template. You can use all the space except where the return label and stamp will go.

Target Market(s)

Target is schools and teachers

Industry/Entity Type

Teacher

```html
<!DOCTYPE html>
<html lang="en">
<head>
<meta charset="utf-8">
<title>Free Chair Massage Postcard</title>
<link href="https://fonts.googleapis.com/css2?family=Arimo:wght@400;700&display=swap" rel="stylesheet">
<style>
  :root {
    --page-bg: #e9e7e4;
    --card-white: #ffffff;
    --brand-blue: #1b4f9f;
    --brand-green: #6aa843;
    --text-gray: #58595b;
    --photo-light: #f1f2f3;
    --photo-mid: #c9ced6;
    --photo-deep: #7d8899;
  }
  * { box-sizing: border-box; margin: 0; padding: 0; }
  html, body {
    width: 1200px; height: 846px; overflow: hidden;
    background: var(--page-bg);
    font-family: "Arimo", Arial, sans-serif;
  }
  .postcard {
    position: absolute; left: 162px; top: 132px;
    width: 870px; height: 614px;
    background: var(--card-white);
    overflow: hidden;
  }
  .hero-photo {
    position: absolute; left: 0; top: 0;
    width: 520px; height: 290px;
    background:
      linear-gradient(90deg, rgba(255,255,255,0) 55%, var(--card-white) 100%),
      radial-gradient(ellipse at 28% 55%, var(--photo-deep) 0%, var(--photo-mid) 38%, var(--photo-light) 75%);
  }
  .headline {
    position: absolute; right: 36px; top: 30px;
    text-align: right; color: var(--brand-blue);
    font-weight: 700; font-size: 64px; line-height: 66px;
    letter-spacing: 0.5px;
  }
  .subhead {
    position: absolute; right: 36px; top: 166px;
    text-align: right; color: var(--text-gray);
    font-weight: 700; font-size: 29px; line-height: 37px;
  }
  .info-band {
    position: absolute; left: 0; top: 290px;
    width: 100%; height: 166px;
    background: var(--brand-green);
    color: #fff; font-size: 18.5px; line-height: 23px;
    padding: 20px 20px 0 228px;
  }
  .info-band p + p { margin-top: 12px; }
  .info-band strong { font-weight: 700; }
  .cta-band {
    position: absolute; left: 0; top: 456px;
    width: 100%; height: 42px;
    background: var(--brand-blue);
    color: #fff; text-align: center;
    font-size: 25px; line-height: 42px;
  }
  .cta-band strong { font-weight: 700; }
  .appreciation-badge {
    position: absolute; left: 22px; top: 244px;
    width: 176px; height: 176px; border-radius: 50%;
    background: var(--brand-blue);
    border: 6px solid var(--card-white);
    display: flex; align-items: center; justify-content: center;
  }
  .appreciation-badge span {
    display: block; transform: rotate(-22deg);
    color: #fff; font-weight: 700; font-size: 18px; line-height: 21px;
    text-align: center;
  }
  .contact {
    position: absolute; left: 42px; top: 516px;
  }
  .phone {
    display: flex; align-items: center; gap: 6px;
    color: var(--brand-green); font-weight: 700;
    font-size: 46px; line-height: 52px;
  }
  .website {
    margin: 4px 0 0 78px;
    color: var(--brand-blue); font-weight: 700; font-size: 22px;
  }
  .company-name {
    position: absolute; left: 556px; top: 512px;
    display: flex; align-items: center; gap: 10px;
  }
  .company-name .mark {
    width: 66px; height: 66px; border-radius: 50%;
    background: var(--brand-blue);
  }
  .company-name span {
    color: var(--text-gray); font-size: 27px; line-height: 29px;
  }
</style>
</head>
<body>
  <main class="postcard">
    <div class="hero-photo" role="img" aria-label="Therapist giving a seated chair massage to a man in a massage chair"></div>

    <h1 class="headline">FREE CHAIR<br>MASSAGE</h1>
    <h2 class="subhead">AT YOUR NEXT SCHOOL<br>IMPROVEMENT &amp;<br>TEACHER INSTITUTE DAY</h2>

    <section class="info-band">
      <p>Call to arrange complimentary chair massages with <strong>VitalPath Wellness Centers</strong>. We will send one of our affiliate therapists to your school and provide chair massages to <strong>Teachers and Staff</strong>.</p>
      <p><strong>Massage helps</strong> relax tight and stiff muscles melting away stress. The therapist aims to release chronic stiffness in the <strong>neck</strong> and <strong>back</strong>.</p>
    </section>

    <div class="appreciation-badge">
      <span>IT'S OUR<br>WAY TO SHOW<br>APPRECIATION<br>TO THE<br>TEACHERS</span>
    </div>

    <div class="cta-band"><strong>CALL TODAY</strong> TO RESERVE A DATE FOR YOUR <strong>SCHOOL</strong></div>

    <div class="contact">
      <div class="phone">
        <svg width="38" height="38" viewBox="0 0 38 38" aria-hidden="true">
          <circle cx="19" cy="19" r="17" fill="none" stroke="#6aa843" stroke-width="2.5"/>
          <path d="M14 10c1.5-.8 2.5 0 3 1.3l1 2.6c.3 1-.2 1.6-1 2.1-.6.4-.6 1 0 2.3.8 1.8 1.8 3.2 3 4 .8.5 1.3.4 1.8-.2.6-.7 1.3-1 2.2-.5l2.3 1.4c1 .6 1.1 1.7.3 2.7-1.5 1.8-4 1.8-6.5.2-3.3-2.1-5.8-6-6.8-9.6-.6-2.3-.3-5 .7-6.3z" fill="#6aa843"/>
        </svg>
        1-800-555-0148
      </div>
      <div class="website">VitalPathWellness.com</div>
    </div>

    <div class="company-name">
      <div class="mark"></div>
      <span>VitalPath<br>Wellness Centers</span>
    </div>
  </main>
</body>
</html>
```